Label - Australian Extra Virgin Olive Oil

I'm seeking a front and back label to apply to bottles/tins of my olive oil. They will be applied to green bottles of various sizes and also white tins. The labels will have the dimensions 70 x 120mm and printed at 600dpi on adhesive labels with metalised backing. With this material, any area which is not colored on the label will show through as silver - the design may make use of this feature. There are some obligatory labeling requirements in Australia including a logo showing the proportion of Australian content, and an indication of the harvest date - the design will need to make allowance for this. Also, since the label will be used in subsequent years and on various sizes of product, I need to be able to alter this with each print run.I have a logo to use on the front label and another I would like to use on the back as this latter one will tie in with other future products (non olive oil).
The text for the back label
"Tallowind Creek is a family run enterprise. Our olives are grown on the banks of the Yarrabell River in Central Victoria and processed locally
email; swiftwombat@kelpo.com.au
text needed for the front label design
"Australian Extra-Virgin Olive Oil"

```html
<!DOCTYPE html>
<html lang="en">
<head>
<meta charset="utf-8">
<title>Tallowind Creek – Australian Extra-Virgin Olive Oil Label</title>
<link rel="stylesheet" href="https://fonts.googleapis.com/css2?family=Cormorant+SC:wght@500;600&family=Courier+Prime&family=Pinyon+Script&display=swap">
<style>
  :root {
    --label-black: #232426;
    --label-edge: #1b1c1e;
    --brand-gold: #b8a24a;
    --rule-amber: #c2862f;
    --type-white: #ecebe6;
    --type-grey: #cfcdc6;
  }
  * { margin: 0; padding: 0; box-sizing: border-box; }
  html, body {
    width: 1200px;
    height: 2614px;
    overflow: hidden;
    background: var(--label-edge);
  }
  .front-label {
    position: relative;
    width: 1200px;
    height: 2614px;
    overflow: hidden;
    background: var(--label-black);
    color: var(--type-white);
    text-align: center;
  }
  .brand-mark {
    position: absolute;
    top: 210px;
    left: 0;
    width: 100%;
    display: flex;
    flex-direction: column;
    align-items: center;
    gap: 50px;
  }
  .brand-dot {
    width: 150px;
    height: 150px;
    border-radius: 50%;
    background: var(--brand-gold);
  }
  .brand-name {
    font-family: "Cormorant SC", serif;
    font-weight: 600;
    font-size: 84px;
    line-height: 1;
    letter-spacing: 5px;
    color: var(--brand-gold);
  }
  .origin {
    position: absolute;
    top: 1000px;
    left: 0;
    width: 100%;
    font-family: "Pinyon Script", cursive;
    font-size: 235px;
    line-height: 1.2;
    color: var(--type-white);
    white-space: nowrap;
  }
  .grade {
    position: absolute;
    top: 1345px;
    right: 310px;
    font-family: "Courier Prime", monospace;
    font-size: 66px;
    line-height: 1;
    letter-spacing: 2px;
    color: var(--type-grey);
  }
  .product-name {
    position: absolute;
    top: 1450px;
    left: 0;
    width: 100%;
    font-family: "Cormorant SC", serif;
    font-weight: 500;
    font-size: 210px;
    line-height: 1;
    letter-spacing: 3px;
    color: var(--type-white);
    white-space: nowrap;
  }
  .process {
    position: absolute;
    top: 1820px;
    left: 160px;
    width: 880px;
    padding: 46px 0;
    border-top: 6px solid var(--rule-amber);
    border-bottom: 6px solid var(--rule-amber);
    font-family: "Courier Prime", monospace;
    font-size: 60px;
    letter-spacing: 5px;
    line-height: 1;
    color: var(--type-grey);
  }
  .volume {
    position: absolute;
    top: 2370px;
    left: 0;
    width: 100%;
    font-family: "Cormorant SC", serif;
    font-weight: 500;
    font-size: 96px;
    line-height: 1;
    letter-spacing: 4px;
    color: var(--type-white);
  }
</style>
</head>
<body>
  <main class="front-label">
    <div class="brand-mark">
      <span class="brand-dot"></span>
      <span class="brand-name">Tallowind Creek</span>
    </div>
    <p class="origin">Australian</p>
    <p class="grade">EXTRA-VIRGIN</p>
    <h1 class="product-name">Olive Oil</h1>
    <p class="process">COLD PRESSED</p>
    <p class="volume">Vol. 750ml</p>
  </main>
</body>
</html>
```